Halden & Pruitt Periodontics and Implant Solutions Business Card

We are a specialty dental practice- implants and periodontal surgery. We have just re-designed our logo and are building a new office and would like to re-design our business card. We are looking for something professional with a creative and artsy twist- something to stand out among the rest! Happy Designing!

I have uploaded all versions of our new logo and our current business card. We have 3 locations and 2 doctors.

Target Market(s)

55+

Industry/Entity Type

Dental

Contact Information for Business Card

Needs Names, logo, locations- professional and artsy!

Colors
0555a3
0592cd
34a7d7
3277b5
85cae6
85acd3
cee9f5
ecf7fb

Requirements
Must have
• our names:
• Thomas E. Halden D.M.D.
• Celia M. Pruitt D.M.D.
• Diplomate of the National Council of Gum Surgery
• Address locations:
• 462 W. Larkspur Avenue Suite 210B Plantation, FL 33871
• Tel: 954-318-2264 Fax: 954-318-2291
• 5127 Harlow Lane #C-4 Boca Raton, FL 33609
• Tel: 561-627-1958 Fax: 561-703-2816
• 274 Northwest 9th Street #412 Miami FL 33987
• Tel: 786-429-6153 Fax: 786-429-6170
Nice to have
• unique look
Should not have
• doesn't need QR like our current card has.

```html
<!DOCTYPE html>
<html lang="en">
<head>
<meta charset="UTF-8">
<title>Halden &amp; Pruitt Business Card</title>
<link href="https://fonts.googleapis.com/css2?family=Open+Sans:wght@400;600;700&display=swap" rel="stylesheet">
<style>
  :root {
    --page-bg: #e9edf2;
    --navy-deep: #14175a;
    --navy-mid: #23287a;
    --navy-light: #2e3590;
    --brand-blue: #0555a3;
    --sky-blue: #85acd3;
    --pale-blue: #cee9f5;
    --white: #ffffff;
    --silver: #b9bcc8;
    --rule-grey: #c9ccd4;
  }
  * { margin: 0; padding: 0; box-sizing: border-box; }
  html, body {
    width: 1200px; height: 784px; overflow: hidden;
    background: var(--page-bg);
    font-family: "Open Sans", Arial, sans-serif;
  }
  .icon-defs { position: absolute; width: 0; height: 0; }
  .canvas {
    position: relative; width: 1200px; height: 784px;
  }
  .card {
    position: absolute; top: 237px;
    width: 540px; height: 310px;
    border-radius: 4px; overflow: hidden;
    box-shadow: 0 6px 18px rgba(20, 23, 90, 0.22);
  }
  .card-back {
    left: 45px;
    background: radial-gradient(ellipse at 70% 30%, var(--navy-light) 0%, var(--navy-mid) 45%, var(--navy-deep) 100%);
  }
  .card-front { left: 615px; background: var(--navy-mid); }

  /* back side */
  .location-list { position: absolute; left: 34px; top: 38px; color: var(--white); }
  .location { margin-bottom: 22px; }
  .location-line { display: flex; align-items: center; font-size: 13.5px; line-height: 22px; white-space: nowrap; }
  .location-line svg { width: 17px; height: 17px; margin-right: 7px; flex: none; }
  .number-pair { display: flex; gap: 20px; }
  .number-pair span { display: flex; align-items: center; }
  .back-mark {
    position: absolute; right: 28px; bottom: 40px;
    display: flex; align-items: center; gap: 7px;
  }
  .back-mark-circle {
    width: 30px; height: 30px; border-radius: 50%;
    border: 1.5px solid var(--white);
  }
  .back-mark-name {
    color: var(--white); font-weight: 600; font-size: 10px; line-height: 12px;
  }
  .back-mark-name small { display: block; font-size: 6.5px; line-height: 9px; }

  /* front side */
  .front-shape { position: absolute; inset: 0; width: 540px; height: 310px; }
  .front-mark {
    position: absolute; left: 0; right: 0; top: 34px;
    display: flex; align-items: center; justify-content: center; gap: 12px;
  }
  .front-mark-circle {
    width: 78px; height: 78px; border-radius: 50%;
    border: 5px solid var(--sky-blue); opacity: 0.7;
  }
  .front-mark-name {
    color: var(--brand-blue); font-weight: 600; font-size: 27px; line-height: 30px; letter-spacing: 0.5px;
  }
  .front-mark-name small { display: block; font-size: 11.5px; line-height: 16px; letter-spacing: 0; }
  .doctor-block {
    position: absolute; left: 0; right: 0; top: 168px; text-align: center;
    color: var(--silver); font-weight: 600;
  }
  .doctor-name { font-size: 15px; line-height: 19px; letter-spacing: 0.4px; }
  .doctor-credential { font-size: 10.5px; line-height: 16px; letter-spacing: 0.4px; margin-top: 2px; }
  .front-contact { position: absolute; right: 34px; top: 232px; color: var(--white); }
  .main-phone { display: flex; align-items: center; justify-content: flex-end; font-size: 20px; font-weight: 600; }
  .main-phone svg { width: 20px; height: 20px; margin-right: 7px; }
  .web-line { display: flex; gap: 16px; font-size: 11.5px; margin-top: 6px; }
  .web-line span { display: flex; align-items: center; }
  .web-line svg { width: 14px; height: 14px; margin-right: 5px; }
</style>
</head>
<body>
<svg class="icon-defs" aria-hidden="true">
  <defs>
    <symbol id="icon-pin" viewBox="0 0 20 20">
      <circle cx="10" cy="10" r="9.5" fill="#ffffff"/>
      <path d="M10 4a4 4 0 0 0-4 4c0 3 4 7.5 4 7.5s4-4.5 4-7.5a4 4 0 0 0-4-4zm0 5.5a1.5 1.5 0 1 1 0-3 1.5 1.5 0 0 1 0 3z" fill="#23287a"/>
    </symbol>
    <symbol id="icon-phone" viewBox="0 0 20 20">
      <circle cx="10" cy="10" r="9.5" fill="#ffffff"/>
      <path d="M7 5l2 2.5-1.2 1.3a7 7 0 0 0 3.4 3.4l1.3-1.2L15 13l-1 1.8c-4.5 0-8.8-4.3-8.8-8.8z" fill="#23287a"/>
    </symbol>
    <symbol id="icon-fax" viewBox="0 0 20 20">
      <rect x="0.5" y="1.5" width="19" height="17" rx="4" fill="#ffffff"/>
      <rect x="6" y="4.5" width="8" height="4" fill="#23287a"/>
      <rect x="4" y="9" width="12" height="6" rx="1" fill="#23287a"/>
    </symbol>
    <symbol id="icon-globe" viewBox="0 0 20 20">
      <circle cx="10" cy="10" r="8.5" fill="none" stroke="#ffffff" stroke-width="1.6"/>
      <ellipse cx="10" cy="10" rx="3.5" ry="8.5" fill="none" stroke="#ffffff" stroke-width="1.3"/>
      <line x1="1.5" y1="10" x2="18.5" y2="10" stroke="#ffffff" stroke-width="1.3"/>
    </symbol>
    <symbol id="icon-at" viewBox="0 0 20 20">
      <circle cx="10" cy="10" r="8.5" fill="none" stroke="#ffffff" stroke-width="1.6"/>
      <circle cx="10" cy="10" r="3" fill="none" stroke="#ffffff" stroke-width="1.6"/>
      <path d="M13 7.5v3.5a1.8 1.8 0 0 0 3.5 0" fill="none" stroke="#ffffff" stroke-width="1.6"/>
    </symbol>
  </defs>
</svg>

<main class="canvas">
  <section class="card card-back" aria-label="Card back with office locations">
    <div class="location-list">
      <div class="location">
        <div class="location-line"><svg><use href="#icon-pin"/></svg>462 W. Larkspur Avenue Suite 210B Plantation, FL 33871</div>
        <div class="location-line number-pair">
          <span><svg><use href="#icon-phone"/></svg>954-318-2264</span>
          <span><svg><use href="#icon-fax"/></svg>954-318-2291</span>
        </div>
      </div>
      <div class="location">
        <div class="location-line"><svg><use href="#icon-pin"/></svg>5127 Harlow Lane #C-4 Boca Raton, FL 33609</div>
        <div class="location-line number-pair">
          <span><svg><use href="#icon-phone"/></svg>561-627-1958</span>
          <span><svg><use href="#icon-fax"/></svg>561-703-2816</span>
        </div>
      </div>
      <div class="location">
        <div class="location-line"><svg><use href="#icon-pin"/></svg>274 Northwest 9th Street #412 Miami FL 33987</div>
        <div class="location-line number-pair">
          <span><svg><use href="#icon-phone"/></svg>786-429-6153</span>
          <span><svg><use href="#icon-fax"/></svg>786-429-6170</span>
        </div>
      </div>
    </div>
    <div class="back-mark">
      <div class="back-mark-circle"></div>
      <div class="back-mark-name">HALDEN &amp; PRUITT<small>Periodontics and Implant Solutions</small></div>
    </div>
  </section>

  <section class="card card-front" aria-label="Card front with doctors and main contact">
    <svg class="front-shape" viewBox="0 0 540 310" preserveAspectRatio="none" aria-hidden="true">
      <defs>
        <linearGradient id="front-navy" x1="0" y1="0" x2="0" y2="1">
          <stop offset="0" stop-color="#2e3590"/>
          <stop offset="1" stop-color="#14175a"/>
        </linearGradient>
      </defs>
      <rect width="540" height="310" fill="url(#front-navy)"/>
      <path d="M0 0H540V38C470 40 430 88 360 118C280 150 140 152 0 138Z" fill="#ffffff"/>
      <path d="M0 138C140 152 280 150 360 118C430 88 470 40 540 38" fill="none" stroke="#c9ccd4" stroke-width="4"/>
    </svg>
    <div class="front-mark">
      <div class="front-mark-circle"></div>
      <div class="front-mark-name">HALDEN &amp; PRUITT<small>Periodontics and Implant Solutions</small></div>
    </div>
    <div class="doctor-block">
      <p class="doctor-name">THOMAS E. HALDEN D.M.D.</p>
      <p class="doctor-name">CELIA M. PRUITT D.M.D.</p>
      <p class="doctor-credential">DIPLOMATE OF THE NATIONAL COUNCIL OF GUM SURGERY</p>
    </div>
    <div class="front-contact">
      <div class="main-phone"><svg><use href="#icon-phone"/></svg>954-318-2264</div>
      <div class="web-line">
        <span><svg><use href="#icon-globe"/></svg>www.haldenperio.com</span>
        <span><svg><use href="#icon-at"/></svg>contactus.haldenperio.com</span>
      </div>
    </div>
  </section>
</main>
</body>
</html>
```